Law Offices business card

Hi there, I'll need business card for the Law Offices of Tobin Haskell. The information must convey his strategic approach and quick resolution to complex business litigation needs. Please emphasize Civil Litigation, Corporate Law, Business Governance and Real Estate Law. Tobin has over 25 years of experience in these fields.The card should be modern and edgy and the message should be clear. Please consult his current website for ideas.

Business

```html
<!DOCTYPE html>
<html lang="en">
<head>
<meta charset="utf-8">
<title>Law Offices of Tobin Haskell – Business Card</title>
<link rel="stylesheet" href="https://fonts.googleapis.com/css2?family=Tinos:wght@400;700&family=Arimo:wght@400;700&display=swap">
<style>
  :root {
    --backdrop: #e6e3de;
    --card-white: #f7f7f7;
    --ink-black: #0b0b0b;
    --text-dark: #1a1a1a;
    --text-grey: #555555;
    --text-light: #f2f2f2;
    --photo-light: #f1f0ee;
    --photo-mid: #d4d1cc;
  }
  * { margin: 0; padding: 0; box-sizing: border-box; }
  html, body { width: 1200px; height: 902px; overflow: hidden; }
  body {
    background: var(--backdrop);
    display: flex;
    align-items: center;
    justify-content: center;
    gap: 40px;
  }
  .card {
    position: relative;
    width: 540px;
    height: 310px;
    background: var(--card-white);
    overflow: hidden;
    box-shadow: 0 6px 18px rgba(0,0,0,0.18);
  }

  /* Back side */
  .services-photo {
    position: absolute;
    top: 0; right: 0;
    width: 300px; height: 200px;
    background: radial-gradient(ellipse at 55% 45%, var(--photo-mid) 0%, var(--photo-light) 60%, var(--card-white) 100%);
    opacity: 0.8;
  }
  .services-title {
    position: absolute;
    left: 34px; top: 90px;
    font-family: "Tinos", "Times New Roman", serif;
    font-weight: 700;
    font-size: 38px;
    color: var(--text-dark);
  }
  .services-list {
    position: absolute;
    left: 60px; top: 156px;
    list-style: none;
    font-family: "Arimo", Arial, sans-serif;
    font-size: 21px;
    color: var(--text-grey);
  }
  .services-list li {
    display: flex;
    align-items: center;
    gap: 14px;
    margin-bottom: 10px;
  }
  .scale-icon { width: 20px; height: 16px; flex: none; }

  /* Front side */
  .front-shape { position: absolute; inset: 0; }
  .attorney-name {
    position: absolute;
    left: 0; width: 500px; top: 30px;
    text-align: center;
    font-family: "Tinos", "Times New Roman", serif;
    font-weight: 700;
    font-size: 38px;
    color: var(--text-dark);
  }
  .attorney-title {
    position: absolute;
    left: 0; width: 500px; top: 76px;
    text-align: center;
    font-family: "Arimo", Arial, sans-serif;
    font-weight: 700;
    font-size: 20px;
    color: var(--text-dark);
  }
  .firm-name {
    position: absolute;
    left: 0; width: 500px; top: 114px;
    text-align: center;
    font-family: "Tinos", "Times New Roman", serif;
    font-weight: 700;
    font-size: 24px;
    color: var(--text-dark);
  }
  .contact {
    position: absolute;
    left: 160px; width: 340px; top: 218px;
    text-align: center;
    font-family: "Arimo", Arial, sans-serif;
    font-style: normal;
    font-size: 14px;
    line-height: 17px;
    color: var(--text-light);
  }
</style>
</head>
<body>

  <section class="card card-back">
    <div class="services-photo" role="img" aria-label="Faded photo of a graduation cap resting on law books"></div>
    <h2 class="services-title">Srevices :</h2>
    <ul class="services-list">
      <li><svg class="scale-icon" viewBox="0 0 20 16"><g stroke="#555" stroke-width="1.3" fill="none"><line x1="10" y1="2" x2="10" y2="14"/><line x1="3" y1="4" x2="17" y2="4"/><line x1="6" y1="14" x2="14" y2="14"/><path d="M1 9 L3 4 L5 9 Z M15 9 L17 4 L19 9 Z"/></g></svg>Civil Litigation</li>
      <li><svg class="scale-icon" viewBox="0 0 20 16"><g stroke="#555" stroke-width="1.3" fill="none"><line x1="10" y1="2" x2="10" y2="14"/><line x1="3" y1="4" x2="17" y2="4"/><line x1="6" y1="14" x2="14" y2="14"/><path d="M1 9 L3 4 L5 9 Z M15 9 L17 4 L19 9 Z"/></g></svg>Corporate Law</li>
      <li><svg class="scale-icon" viewBox="0 0 20 16"><g stroke="#555" stroke-width="1.3" fill="none"><line x1="10" y1="2" x2="10" y2="14"/><line x1="3" y1="4" x2="17" y2="4"/><line x1="6" y1="14" x2="14" y2="14"/><path d="M1 9 L3 4 L5 9 Z M15 9 L17 4 L19 9 Z"/></g></svg>Business Governance</li>
      <li><svg class="scale-icon" viewBox="0 0 20 16"><g stroke="#555" stroke-width="1.3" fill="none"><line x1="10" y1="2" x2="10" y2="14"/><line x1="3" y1="4" x2="17" y2="4"/><line x1="6" y1="14" x2="14" y2="14"/><path d="M1 9 L3 4 L5 9 Z M15 9 L17 4 L19 9 Z"/></g></svg>Real Estate Law</li>
    </ul>
  </section>

  <section class="card card-front">
    <svg class="front-shape" viewBox="0 0 540 310" preserveAspectRatio="none">
      <defs>
        <linearGradient id="swooshFade" x1="0" x2="1" y1="0" y2="0">
          <stop offset="0" stop-color="#3a3a3a"/>
          <stop offset="0.6" stop-color="#8a8a8a"/>
          <stop offset="1" stop-color="#bdbdbd"/>
        </linearGradient>
      </defs>
      <path d="M0,200 C200,215 420,190 540,100 L540,110 C420,200 200,224 0,207 Z" fill="url(#swooshFade)"/>
      <path d="M0,211 C200,228 420,204 540,116 L540,310 L0,310 Z" fill="var(--ink-black)"/>
    </svg>
    <h1 class="attorney-name">Tobin Haskell</h1>
    <p class="attorney-title">Attorney</p>
    <p class="firm-name">Law Offices of Tobin Haskell, P.A.</p>
    <address class="contact">
      561-430-7718<br>
      561-430-7790<br>
      tobin@haskell-legal.com<br>
      www.haskell-legal.com<br>
      412C Coral Avenue, Palm Beach, Florida 33480
    </address>
  </section>

</body>
</html>
```